Pacific Screen Trade Alliance is preparing a regular newsletter and needs a design

Our association is made up of media companies, TV stations and video on demand companies. As an association our role is to bring industry together to engage in government dialogues, fight video piracy and hold conferences and events. We are starting a regular newsletter to let our members know what activities we have been undertaking on their behalf and what upcoming activities there are. It will be a combination of text and pictures/ graphics. We have made a lot of changes to the association so we need a design which is professional looking, but also creative and future looking. It should also have a sense of entertainment given it is the video entertainment industry we represent. Attached is an example of a recent newsletter but would like to see something a little more dynamic and professional.

Target Market(s)

Executives in media companies

Font styles to use
Serif

Colors

Designer to choose colors to be used in the design.

Requirements
Must have
• A combination of text, photos and graphics in a modern, personable yet professional layout and design

```html
<!DOCTYPE html>
<html lang="en">
<head>
<meta charset="utf-8">
<title>Weekly Newsletter — Pacific Screen Trade Alliance</title>
<link href="https://fonts.googleapis.com/css2?family=Playfair+Display:wght@400;600&display=swap" rel="stylesheet">
<style>
  :root {
    --teal: #08bfc3;
    --ink-dark: #1e2a27;
    --code-green: #23684a;
    --code-bright: #3f9e6e;
    --deep-green: #14221e;
    --white: #ffffff;
  }
  html, body {
    margin: 0;
    padding: 0;
    overflow: hidden;
    background: var(--white);
  }
  .cover {
    position: relative;
    width: 848px;
    height: 1200px;
    overflow: hidden;
    font-family: "Playfair Display", serif;
    color: var(--white);
  }
  .cover__header {
    position: absolute;
    inset: 0 0 auto 0;
    height: 600px;
    background: var(--teal);
  }
  .cover__visual {
    position: absolute;
    top: 600px;
    left: 0;
    width: 848px;
    height: 600px;
    background:
      radial-gradient(ellipse 40% 70% at 42% 45%, rgba(70,170,115,0.40), transparent 70%),
      linear-gradient(100deg,
        var(--deep-green) 0%,
        var(--code-green) 18%,
        var(--deep-green) 28%,
        var(--code-bright) 42%,
        var(--code-green) 55%,
        var(--ink-dark) 75%,
        var(--deep-green) 100%);
  }
  .brand {
    position: absolute;
    top: 70px;
    left: 0;
    width: 100%;
    text-align: center;
    font-size: 22px;
    font-weight: 600;
    letter-spacing: 0.5px;
    line-height: 1.2;
  }
  .title {
    position: absolute;
    left: 0;
    width: 100%;
    margin: 0;
    text-align: center;
    font-size: 62px;
    font-weight: 600;
    letter-spacing: 1px;
    line-height: 1;
  }
  .title--weekly { top: 504px; }
  .title--newsletter { top: 631px; }
  .issue-date {
    position: absolute;
    top: 905px;
    left: 0;
    width: 100%;
    text-align: center;
    font-size: 30px;
    font-weight: 400;
    letter-spacing: 0.5px;
    line-height: 1.2;
  }
</style>
</head>
<body>
  <main class="cover">
    <section class="cover__header">
      <div class="brand">Pacific Screen Trade Alliance</div>
    </section>
    <div class="cover__visual" role="img" aria-label="Close-up photo of streams of green digital code on a dark screen"></div>
    <h1 class="title title--weekly">WEEKLY</h1>
    <h1 class="title title--newsletter">NEWSLETTER</h1>
    <div class="issue-date">04.15.19</div>
  </main>
</body>
</html>
```